Business Card Design - Law Firm

I need a business card design. I have attached a picture of the law firm's website and logo. The business card design should be consistent with those pictures. There should be a place for the employee name, employee job title, telephone number, facsimile number, address, website url, and email address for each employee.
Industry/Entity Type
Business

```html
<!DOCTYPE html>
<html lang="en">
<head>
<meta charset="utf-8">
<title>Whitcombe Law – Business Card</title>
<link rel="stylesheet" href="https://fonts.googleapis.com/css2?family=Libre+Baskerville&family=Open+Sans:wght@400;600;700&display=swap">
<style>
  :root {
    --page: #ffffff;
    --card-grey: #6b6b6b;
    --brand-grey: #707070;
    --ink: #111111;
    --text-grey: #555555;
    --white: #ffffff;
    --border: #2b2b2b;
  }
  * { box-sizing: border-box; margin: 0; padding: 0; }
  html, body { width: 1200px; height: 645px; overflow: hidden; background: var(--page); }
  body { position: relative; font-family: "Open Sans", Arial, sans-serif; color: var(--ink); }

  .side-label {
    position: absolute; font-size: 17px; font-weight: 400; color: var(--ink);
    text-align: center;
  }
  .side-label--front { left: 191px; width: 458px; top: 178px; }
  .side-label--back { left: 776px; width: 262px; top: 72px; }

  .card { position: absolute; }
  .card--front {
    left: 191px; top: 218px; width: 458px; height: 260px;
    background: var(--card-grey);
    display: flex; align-items: center; justify-content: center; gap: 18px;
  }
  .card--back {
    left: 776px; top: 120px; width: 262px; height: 460px;
    background: var(--white); border: 2px solid var(--border);
    text-align: center;
  }

  .brand-square { width: 46px; height: 46px; background: var(--white); }
  .brand-divider { width: 1px; height: 64px; background: var(--white); }
  .brand-name {
    font-family: "Libre Baskerville", Georgia, serif; font-weight: 400;
    color: var(--white); font-size: 24px; letter-spacing: 0.2px; white-space: nowrap;
  }

  .card--back .brand-square {
    position: absolute; left: 108px; top: 48px; width: 44px; height: 44px;
    background: var(--brand-grey);
  }
  .card--back .brand-name {
    position: absolute; left: 0; right: 0; top: 142px;
    color: var(--brand-grey); font-size: 22px;
  }

  .person { position: absolute; left: 0; right: 0; top: 226px; }
  .person__name { font-size: 25px; font-weight: 700; line-height: 1; white-space: nowrap; }
  .person__suffix { font-size: 11px; font-weight: 700; vertical-align: -2px; margin-left: 2px; }
  .person__title { font-size: 11px; font-weight: 700; margin-top: 6px; letter-spacing: 0.2px; }

  .contact { position: absolute; left: 0; right: 0; top: 318px; color: var(--text-grey); }
  .contact__phone { font-size: 15px; font-weight: 700; line-height: 1.2; }
  .contact__fax { font-size: 7px; font-weight: 600; line-height: 1.1; margin-bottom: 4px; }
  .contact__web { font-size: 14.5px; font-weight: 700; line-height: 1.3; }

  .address {
    position: absolute; left: 0; right: 0; top: 410px;
    font-size: 11px; color: var(--text-grey); line-height: 1.4;
    text-transform: uppercase; letter-spacing: 0.2px;
  }
</style>
</head>
<body>
  <div class="side-label side-label--front">Front</div>
  <div class="side-label side-label--back">Back</div>

  <section class="card card--front" aria-label="Card front">
    <div class="brand-square" aria-hidden="true"></div>
    <div class="brand-divider" aria-hidden="true"></div>
    <div class="brand-name">Whitcombe Law</div>
  </section>

  <section class="card card--back" aria-label="Card back">
    <div class="brand-square" aria-hidden="true"></div>
    <div class="brand-name">Whitcombe Law</div>

    <div class="person">
      <div class="person__name">Daniel R. Marsh<span class="person__suffix">ESQ</span></div>
      <div class="person__title">ATTORNEY AT LAW</div>
    </div>

    <div class="contact">
      <div class="contact__phone">+1.555.013.2470</div>
      <div class="contact__fax">Fax+ 1.555.013.2471</div>
      <div class="contact__web">dmarsh@whitcombelaw.com</div>
      <div class="contact__web">whitcombelaw.com</div>
    </div>

    <div class="address">
      48 Elm Court<br>Rivertown, RV
    </div>
  </section>
</body>
</html>
```